Tavo's Spice Blend Dry Roasted and Freshly Ground Spices to create the Authentic and Aromatic Maur

I need a packaging design for a new company based in Kent called Tavo's Spice Blend. the size of the packaging will be for a 250gm bag.

I would like bright colours so that it can stand out from out the other products on a super market shelf

The packaging must have the list of ingredients on the back;

I.e. Ingredients;
Cumin
Coriander
Dried Red Chili
Cinnamon
Cloves
Cardamon
Black Peppercorn
Rice

Reason: Not enough designed to choose from. Tavo's Spice Blend, Dry Roasted and Freshly Ground Spices to create the Authentic and Aromatic flavour Please also add Turmeric to the ingredient list Thank you Bronna Castell

```html
<!DOCTYPE html>
<html lang="en">
<head>
<meta charset="utf-8">
<title>Tavo's Spice Blend – 250 g Pack Front</title>
<link rel="stylesheet" href="https://fonts.googleapis.com/css2?family=Fredoka:wght@700&family=PT+Sans+Narrow:wght@700&display=swap">
<style>
  :root {
    --chili-red: #f52a00;
    --saffron-orange: #ff8005;
    --label-white: #ffffff;
    --ink-black: #0b0b0b;
    --spice-red: #c8230f;
    --spice-orange: #e8561c;
    --spice-brown: #7a3514;
    --spice-umber: #5a2a10;
    --spice-ochre: #8d5a22;
  }
  html, body {
    margin: 0;
    padding: 0;
    width: 1200px;
    height: 1200px;
    overflow: hidden;
    background: var(--label-white);
  }
  .pack-front {
    display: block;
    width: 1200px;
    height: 1200px;
  }
  .product-name {
    font-family: "Fredoka", "Arial Rounded MT Bold", sans-serif;
    font-weight: 700;
    font-size: 120px;
    fill: var(--ink-black);
    letter-spacing: 2px;
  }
  .weight-text {
    font-family: "PT Sans Narrow", "Arial Narrow", sans-serif;
    font-weight: 700;
    font-size: 44px;
    fill: var(--label-white);
  }
</style>
</head>
<body>
<svg class="pack-front" viewBox="0 0 1200 1200" xmlns="http://www.w3.org/2000/svg">
  <defs>
    <linearGradient id="spiceTones" x1="0" y1="0" x2="1" y2="1">
      <stop offset="0" stop-color="var(--spice-red)"/>
      <stop offset="0.35" stop-color="var(--spice-orange)"/>
      <stop offset="0.6" stop-color="var(--spice-brown)"/>
      <stop offset="1" stop-color="var(--spice-umber)"/>
    </linearGradient>
    <radialGradient id="ochreCorner" cx="0.05" cy="0.95" r="0.35">
      <stop offset="0" stop-color="var(--spice-ochre)"/>
      <stop offset="1" stop-color="var(--spice-ochre)" stop-opacity="0"/>
    </radialGradient>
    <filter id="shadowDown" x="-5%" y="-20%" width="110%" height="160%">
      <feDropShadow dx="0" dy="10" stdDeviation="10" flood-color="#000" flood-opacity="0.55"/>
    </filter>
    <filter id="shadowUp" x="-5%" y="-60%" width="110%" height="160%">
      <feDropShadow dx="0" dy="-10" stdDeviation="10" flood-color="#000" flood-opacity="0.55"/>
    </filter>
  </defs>

  <g class="spice-photo" role="img" aria-label="Close-up photograph of heaps of ground red, orange and brown spices">
    <rect x="0" y="640" width="1200" height="560" fill="url(#spiceTones)"/>
    <rect x="0" y="640" width="1200" height="560" fill="url(#ochreCorner)"/>
  </g>

  <rect class="top-field" x="0" y="0" width="1200" height="260" fill="var(--chili-red)"/>

  <path class="name-band" d="M0,320 C250,390 600,370 1200,230 V600 C500,690 200,720 0,640 Z" fill="var(--label-white)"/>

  <path class="wave-upper" filter="url(#shadowDown)" d="M0,225 C300,270 600,230 1200,160 V240 C600,380 250,400 0,335 Z" fill="var(--saffron-orange)"/>

  <path class="wave-lower" filter="url(#shadowUp)" d="M0,620 C200,700 500,680 1200,560 V690 C700,760 300,820 0,745 Z" fill="var(--saffron-orange)"/>

  <g class="product-title">
    <text class="product-name" transform="translate(585 465) rotate(-10)" text-anchor="middle">TAVO'S SPICE</text>
    <text class="product-name" transform="translate(628 598) rotate(-10)" text-anchor="middle">BLEND</text>
  </g>

  <g class="weight-badge">
    <circle cx="112" cy="88" r="80" fill="var(--label-white)"/>
    <circle cx="112" cy="88" r="82" fill="none" stroke="var(--label-white)" stroke-width="9" stroke-linecap="round" stroke-dasharray="0 10.7"/>
    <circle cx="112" cy="88" r="72" fill="var(--ink-black)"/>
    <text class="weight-text" x="112" y="104" text-anchor="middle">250 g</text>
  </g>
</svg>
</body>
</html>
```